依頼詳細
ラフではありますが、pptでチラシ案を作成しました。
要望事項も記載しておりますので、内容のご確認をお願いいたします。
不明点御座いましたら、お気軽にお申し付けください。
記載項目
記載事項もチラシ案に記載しております。
内容のご確認をお願いいたします。
不明点御座いましたら、お気軽にお申し付けください。
サイズ
A4
ページ数
両面
希望イメージ
シンプル 複雑
単色 カラフル
暗い 明るい
日常 高級
遊び心 厳粛
未来的 伝統的
女性的 男性的
希望する色
青系、無彩色系
納品ファイル
• イラストレーター形式 (.ai)
• PNG形式 (.png)
補足説明
aiとpdfでいただけますと幸いです。
ラフ案作成済です。体裁を整えていただく依頼となります。

本件のポイントを的確に捉えて表現いただいたことが決め手になりました。また、全体的なバランスと見やすさを加味して選定をさせていただだきました。

この度は、沢山の素晴らしいご提案をくださいまして、誠にありがとうございました。 素人が作成したラフ案から、こちらの意図を汲み取っていただき、どれも素晴らしい内容で、選考にはとても苦慮いたしましたが、慎重に皆様の提案を一つ一つ確認し、検討させていただきました。 お忙しい中、ご提案頂きましたこと皆様に重ねてお礼申し上げます。 次回ご提案をお願いさせていただく際もよろしくお願いいたします。

```html
<!DOCTYPE html>
<html lang="ja">
<head>
<meta charset="utf-8">
<title>RF×SPA ご案内チラシ</title>
<link rel="stylesheet" href="https://fonts.googleapis.com/css2?family=Noto+Sans+JP:wght@400;500;700;900&display=swap">
<style>
:root{
  --navy:#16307a;
  --blue:#1d5fb8;
  --sky:#dfeefa;
  --red:#d8261e;
  --green:#2f9a44;
  --ink:#222;
  --white:#fff;
}
*{margin:0;padding:0;box-sizing:border-box}
html,body{width:849px;height:1200px;overflow:hidden;background:var(--white)}
body{font-family:"Noto Sans JP",sans-serif;color:var(--ink)}
.flyer{position:relative;width:849px;height:1200px;overflow:hidden}

.brand-bar{height:50px;display:flex;align-items:center;justify-content:space-between;padding:0 26px}
.brand{display:flex;align-items:center;gap:7px;font-weight:700;font-size:15px;color:var(--navy)}
.brand .mark{width:14px;height:14px;background:var(--navy);border-radius:50%}
.brand.sq .mark{border-radius:0;background:var(--green)}
.brand.green{color:var(--green)}

.lead{height:22px;text-align:center;font-weight:700;font-size:17px;color:var(--blue);letter-spacing:.02em}

.hero{position:relative;height:410px;margin-top:2px}
.hero-photo{position:absolute;inset:0;background:linear-gradient(180deg,#c9d6e2 0%,#9fb2c4 35%,#6d7f92 62%,#b6c1cb 100%)}
.hero-copy{position:absolute;inset:0;text-align:center}
.badge{position:absolute;left:38px;top:78px;width:112px;height:112px;border-radius:50%;background:var(--red);color:var(--white);font-weight:900;font-size:30px;line-height:1.1;display:flex;align-items:center;justify-content:center;transform:rotate(-12deg);border:4px solid var(--white)}
.headline{position:absolute;left:165px;top:40px;font-weight:900;color:var(--navy);font-size:104px;letter-spacing:-.02em;line-height:1;-webkit-text-stroke:3px var(--white);paint-order:stroke fill}
.headline small{font-size:56px}
.headline-notes{position:absolute;top:146px;left:0;right:0;font-size:20px;font-weight:700;color:var(--navy)}
.headline-notes .n1{position:absolute;left:208px}
.headline-notes .n2{position:absolute;left:420px}
.headline-sub{position:absolute;top:178px;left:0;right:0;font-weight:900;font-size:56px;color:var(--navy);-webkit-text-stroke:3px var(--white);paint-order:stroke fill}
.salt{position:absolute;top:300px;left:0;right:0;font-weight:900;color:var(--navy);-webkit-text-stroke:3px var(--white);paint-order:stroke fill}
.salt .l1{font-size:44px;display:block}
.salt .l2{font-size:34px;display:block;margin-top:2px}

.damage{display:flex;justify-content:center;gap:22px;margin-top:8px}
.damage figure{width:200px;text-align:center}
.damage .ph{height:104px;border:2px solid var(--white)}
.damage .p1{background:linear-gradient(135deg,#8c8f8a,#5a5e5c)}
.damage .p2{background:linear-gradient(135deg,#a0582e,#6d3b22)}
.damage .p3{background:linear-gradient(135deg,#9b8f80,#6f6658)}
.damage figcaption{font-size:14px;margin-top:6px;color:var(--ink)}

.solution{margin-top:14px;text-align:center;font-weight:900;font-size:31px;line-height:1.4;color:var(--navy)}
.solution em{font-style:normal;color:var(--blue)}

.desc{margin:14px 70px 0;font-size:16px;line-height:1.65;font-weight:500}
.points{margin:8px 70px 0;list-style:none;font-weight:900;font-size:23px;color:var(--red);line-height:1.4}

.scheme{position:relative;margin:14px 40px 0;height:224px}
.provider{position:absolute;left:0;top:20px;width:140px;height:170px;border:2px solid var(--blue);border-radius:8px;display:flex;flex-direction:column;align-items:center;justify-content:center;gap:10px;font-weight:700;color:var(--navy);font-size:14px;text-align:center}
.provider .mark{width:26px;height:26px;background:var(--navy);border-radius:50%}
.flow{position:absolute;left:156px;width:440px}
.flow svg{display:block}
.flow p{font-size:12.5px;line-height:1.45;margin:4px 10px 0;color:var(--ink)}
.flow.f1{top:14px}
.flow.f2{top:104px}
.customer{position:absolute;right:0;top:0;width:150px;text-align:center}
.customer .tag{background:var(--blue);color:var(--white);font-weight:700;font-size:18px;padding:4px 0;border-radius:4px}
.customer .house{height:118px;margin-top:8px;background:linear-gradient(180deg,#cfe3f5,#8fb1d3)}
.customer .supply{font-size:13px;margin-top:6px;font-weight:500}

.footer{position:absolute;left:0;right:0;bottom:0;height:82px;background:var(--sky);display:flex;align-items:center;justify-content:space-between;padding:0 40px}
.company{font-size:12.5px;line-height:1.55}
.company strong{font-size:15px;color:var(--navy)}
.company .grp{color:var(--red);font-weight:700;margin-left:10px}
.transfer{background:var(--red);color:var(--white);font-weight:900;font-size:22px;padding:8px 18px;border-radius:6px}
</style>
</head>
<body>
<div class="flyer">
  <header class="brand-bar">
    <div class="brand"><span class="mark"></span>株式会社彩光テクノロジー</div>
    <div class="brand">あおぞらエナジー・パートナーズ</div>
    <div class="brand sq green"><span class="mark"></span>再エネ宣言ネットワーク</div>
  </header>
  <p class="lead">太陽光設置に興味はあるけど屋根の劣化で諦めているお客様へ</p>

  <section class="hero">
    <div class="hero-photo" role="img" aria-label="工場の屋根に並ぶ太陽光パネルの写真"></div>
    <div class="hero-copy">
      <div class="badge">業界<br>初!!</div>
      <h1 class="headline">RF<small>×</small>SPA<small>が</small></h1>
      <div class="headline-notes"><span class="n1">(屋根補修)</span><span class="n2">(イニシャル費ゼロの太陽光)</span></div>
      <p class="headline-sub">お悩みを解決します!!</p>
      <p class="salt"><span class="l1">重塩害地域で</span><span class="l2">設置が困難なお客様もご相談ください</span></p>
    </div>
  </section>

  <section class="damage">
    <figure><div class="ph p1" role="img" aria-label="割れたスレート屋根の写真"></div><figcaption>割れている</figcaption></figure>
    <figure><div class="ph p2" role="img" aria-label="錆びた金属屋根の写真"></div><figcaption>錆びている</figcaption></figure>
    <figure><div class="ph p3" role="img" aria-label="欠けのある屋根材の写真"></div><figcaption>割れ、欠けがある</figcaption></figure>
  </section>

  <h2 class="solution"><em>RF×SPA</em>は屋根補修と太陽光発電システムを<br>組み合わせた新しいソリューションです。</h2>

  <p class="desc">お客様の屋根を補修した上で、屋根上に太陽光発電システムを設置・保守・管理<br>（発電設備の所有権は、あおぞらエナジー・パートナーズが保有します）</p>
  <ul class="points">
    <li>●環境対策と屋根補修が一度に実現!!</li>
    <li>●電気代高騰の今がチャンス!!</li>
  </ul>

  <section class="scheme">
    <div class="provider"><span class="mark"></span>あおぞら<br>エナジー・<br>パートナーズ</div>
    <div class="flow f1">
      <svg width="440" height="34" viewBox="0 0 440 34"><polygon points="0,4 410,4 410,0 440,17 410,34 410,30 0,30" fill="#2f9a44"/><text x="200" y="23" text-anchor="middle" font-family="Noto Sans JP, sans-serif" font-weight="700" font-size="16" fill="#fff">イニシャル費用ゼロで太陽光</text></svg>
      <p>当社が屋根補修と太陽光発電システムを設置・保守・管理</p>
    </div>
    <div class="flow f2">
      <svg width="440" height="34" viewBox="0 0 440 34"><polygon points="440,4 30,4 30,0 0,17 30,34 30,30 440,30" fill="#1d5fb8"/><text x="240" y="23" text-anchor="middle" font-family="Noto Sans JP, sans-serif" font-weight="700" font-size="16" fill="#fff">再エネ導入で御社のイメージアップ</text></svg>
      <p>太陽光で発電した電気を毎月お支払いいただきます。<br>（上記の屋根補修工事費用も含む）</p>
    </div>
    <div class="customer">
      <div class="tag">お客様</div>
      <div class="house" role="img" aria-label="太陽光パネルを載せた建物のイラスト"></div>
      <p class="supply">発電した電気を供給</p>
    </div>
  </section>

  <footer class="footer">
    <div class="company">
      <strong>(株)あおぞらエナジー・パートナーズ</strong><span class="grp">※彩光グループ</span><br>
      設立：2020年4月1日　資本金：5,000万円（株主構成：50%ずつ出資）<br>
      本社：東京都港区青葉台1-2-3
    </div>
    <div class="transfer">20年後に設備譲渡</div>
  </footer>
</div>
</body>
</html>
```